4 Flyers For Health And Wellness Business

I need four different flyers to promote my business and different programs.

One is for a program I am starting to help empower young women to heal traumas and learn to self love. It will incorporate lectures, recipes, yoga classes, guided meditations and my toolbox for loving yourself. All will be done in a group setting. I have not figured out the price yet or exact days. I'd like it to be very pretty, girly and fun!

The second flyer is for a new group coaching option I have for my business. This incorporates all that I do in a one-one relationship with clients offered in the 3 month program (description is in my website www.dovanthia.com ). The price will be 250$/person. Location has not been determined yet. This flyer should look cozy and encouraging. We will most likely be meeting in a coffee shop or yoga studio.

Next, would be a flyer for Corporate Wellness. This would be a call to action flyer describing the benefits of healthy employees and business. The look here should be clean and fresh.

Finally, I'd like to get another flyer that encourages people to sign up for a free 50 minute health consultation and take the step to sign up for one of my programs. Again these are one-on-one online or in person. This flyer should also be fun and eye catching.

Target Market(s)

Women ages 18-55

Industry/Entity Type

Health And Wellness

Font styles to use
Serif
Sans Serif
Script

Requirements
Must have
• Women Flyer: Beautiful, eye catching, call to action (sign up with a friend and get 50$ off)
• Online coaching: (don't need to leave your house) (sign up for your free health consultation now.. Link to website www.dovanthia.com)
• Group coaching: support, recipes, yoga, fun, cozy.
• Call to action: Simple, fun and eye catching. Sign up now, (link to website)
Nice to have
• Flowers, modern, beautiful
• Funny for call to action flyer.
Should not have
• Swearing.

```html
<!DOCTYPE html>
<html lang="en">
<head>
<meta charset="utf-8">
<title>Dovanthia Wellness – Empowering Women</title>
<link href="https://fonts.googleapis.com/css2?family=Montserrat:wght@200;300;700;800;900&display=swap" rel="stylesheet">
<style>
  :root{
    --cream:#efeee3;
    --ink:#333335;
    --grey:#6d6e70;
    --soft-grey:#8a8b8d;
    --green:#8dc63f;
    --badge:#3b3128;
    --gold:#c9a24a;
    --gold-light:#f1d98a;
    --white:#ffffff;
  }
  html,body{margin:0;padding:0;overflow:hidden;background:#ddd;}
  .flyer{
    position:relative;width:848px;height:1200px;overflow:hidden;
    background:var(--white);
    font-family:"Montserrat",sans-serif;color:var(--ink);
  }
  .backdrop{position:absolute;inset:0;}
  .brand{position:absolute;left:42px;top:80px;}
  .brand-dot{width:90px;height:90px;border-radius:50%;background:var(--green);margin-left:120px;margin-bottom:18px;}
  .brand-name{margin:0;font-weight:300;color:var(--grey);font-size:80px;line-height:0.95;letter-spacing:-1px;}
  .brand-name span{display:block;}
  .brand-name .first{font-size:46px;letter-spacing:1px;margin-bottom:6px;}
  .headline{position:absolute;left:0;top:0;margin:0;font-weight:normal;}
  .headline span{position:absolute;white-space:nowrap;color:var(--ink);}
  .h-empower{left:68px;top:440px;font-size:64px;font-weight:800;letter-spacing:-1px;}
  .h-women{left:150px;top:462px;font-size:136px;font-weight:800;letter-spacing:-4px;}
  .h-heal{left:66px;top:585px;font-size:56px;font-weight:200;letter-spacing:-1px;}
  .h-learn{left:110px;top:648px;font-size:56px;font-weight:200;letter-spacing:-1px;}
  .h-self{left:334px;top:636px;font-size:92px;font-weight:800;letter-spacing:-2px;}
  .offer{position:absolute;left:40px;top:710px;width:300px;height:300px;}
  .offer svg{position:absolute;inset:0;}
  .offer-text{
    position:absolute;left:0;top:0;width:300px;height:300px;
    display:flex;flex-direction:column;align-items:center;justify-content:center;
    transform:rotate(-14deg);color:var(--white);font-weight:700;text-align:center;
    text-shadow:1px 2px 3px rgba(0,0,0,.5);
  }
  .offer-text .line{font-size:27px;line-height:1.05;}
  .offer-text .amount{font-size:74px;font-weight:900;line-height:1;margin-top:2px;}
  .offer-text .amount small{font-size:22px;font-weight:700;vertical-align:top;position:relative;top:14px;}
  .contact{position:absolute;left:95px;top:1045px;font-size:16px;font-weight:700;color:#555;line-height:1.3;}
</style>
</head>
<body>
<main class="flyer">
  <svg class="backdrop" width="848" height="1200" viewBox="0 0 848 1200">
    <defs>
      <linearGradient id="portraitTone" x1="0" y1="0" x2="1" y2="1">
        <stop offset="0" stop-color="#5a3a26"/>
        <stop offset="0.5" stop-color="#8a6a55"/>
        <stop offset="1" stop-color="#2c3550"/>
      </linearGradient>
      <linearGradient id="saladTone" x1="0" y1="0" x2="1" y2="0">
        <stop offset="0" stop-color="#d9d2c4"/>
        <stop offset="0.35" stop-color="#ecebe6"/>
        <stop offset="1" stop-color="#f4f4f2"/>
      </linearGradient>
      <linearGradient id="fruitTone" x1="0" y1="0" x2="1" y2="1">
        <stop offset="0" stop-color="#eef0f1"/>
        <stop offset="0.45" stop-color="#f3c2a6"/>
        <stop offset="0.7" stop-color="#e9a86a"/>
        <stop offset="1" stop-color="#f4e6b0"/>
      </linearGradient>
    </defs>
    <polygon points="0,0 600,0 355,362 0,362" fill="var(--cream)"/>
    <polygon points="600,0 848,0 848,600 600,362 355,362" fill="url(#portraitTone)" role="img" aria-label="Portrait of the wellness coach smiling in a home kitchen"/>
    <polygon points="0,362 600,362 848,600 848,800 0,800" fill="url(#saladTone)" role="img" aria-label="Faded photo of a fresh salad bowl on a white wooden table"/>
    <rect x="0" y="800" width="848" height="400" fill="url(#fruitTone)" role="img" aria-label="Photo of watermelon, citrus slices, peach and iced fruit drinks"/>
    <polygon points="0,828 48,828 48,880 0,985" fill="var(--green)"/>
    <polygon points="0,1030 170,1200 0,1200" fill="var(--soft-grey)"/>
  </svg>

  <div class="brand">
    <div class="brand-dot"></div>
    <p class="brand-name"><span class="first">Dovanthia</span><span>Wellness</span></p>
  </div>

  <h1 class="headline">
    <span class="h-empower">EMPOWERING</span>
    <span class="h-women">women</span>
    <span class="h-heal">to heal traumas and</span>
    <span class="h-learn">learn to</span>
    <span class="h-self">self love</span>
  </h1>

  <div class="offer">
    <svg width="300" height="300" viewBox="0 0 300 300">
      <g transform="translate(150 150)" fill="var(--gold)">
        <rect x="-118" y="-118" width="236" height="236"/>
        <rect x="-118" y="-118" width="236" height="236" transform="rotate(15)"/>
        <rect x="-118" y="-118" width="236" height="236" transform="rotate(30)"/>
        <rect x="-118" y="-118" width="236" height="236" transform="rotate(45)"/>
        <rect x="-118" y="-118" width="236" height="236" transform="rotate(60)"/>
        <rect x="-118" y="-118" width="236" height="236" transform="rotate(75)"/>
      </g>
      <g transform="translate(150 150)" fill="var(--badge)">
        <rect x="-107" y="-107" width="214" height="214" transform="rotate(7.5)"/>
        <rect x="-107" y="-107" width="214" height="214" transform="rotate(22.5)"/>
        <rect x="-107" y="-107" width="214" height="214" transform="rotate(37.5)"/>
        <rect x="-107" y="-107" width="214" height="214" transform="rotate(52.5)"/>
        <rect x="-107" y="-107" width="214" height="214" transform="rotate(67.5)"/>
        <rect x="-107" y="-107" width="214" height="214" transform="rotate(82.5)"/>
      </g>
    </svg>
    <div class="offer-text">
      <span class="line">Sign up</span>
      <span class="line">with a friend</span>
      <span class="line">and get</span>
      <span class="amount">50$<small>off</small></span>
    </div>
  </div>

  <address class="contact" style="font-style:normal">
    dovanthiawellness@mail.com<br>
    www.dovanthia.com
  </address>
</main>
</body>
</html>
```